KPI Management Software from Brenwick

We need three ad banners for a campaign about our Key Performance Indicator (KPI) software. The product is called tallyway. You can find all of the information you require about the product here: https://www.brenwick-example.com/kpi-software/

The banner can be animated or static.

The banners will be used by Pindara and Vextor PromoLink and should be the following dimensions and be less than 45kb:

Leaderboard - 728x90
Tower - 120x600
Rectangle - 300x250

The banner design should be in keeping with the website and include the brenwick logo, Various formats of the logo are attached. The words/phases should be included:

'Brenwick' (use the logo)
'KPI Software'
'Free Trial'
optionally 'Tallyway'

This is a business to business service, NOT a consumer service, and therefore the banners should lean towards a more corporate style.

We have recently gone live with a new website:

http://www.brenwick-example.com. The ads should be in the same style as the website and can draw on any of the graphics you see.

Pindara requires the animation to cease after a maximum of 30 seconds.

Pindara has a further restriction: "Any ads featuring a white or black background are required to have a 1 px border of a distinguishing color around the perimeter of the ad in order to separate it from page content."

For all Pindara restrictions please see: http://support.pindara-example.com/creative-requirements/

Target Market(s)

Businesses medium to large, the oveall feel should be business to business corpoate not consumer.

Requirements
Must have
• Must focus on the phrase "KPI Software'
Nice to have
• This could be an animated banner, but it is not essential

```html
<!DOCTYPE html>
<html lang="en">
<head>
<meta charset="utf-8">
<title>KPI Management Software – Ad Banner Set</title>
<link rel="stylesheet" href="https://fonts.googleapis.com/css2?family=Open+Sans:wght@400;600&family=PT+Sans:wght@700&family=PT+Sans+Narrow:wght@400;700&display=swap">
<style>
  :root {
    --brand-red: #ec1c24;
    --panel-dark: #2a2a2c;
    --panel-black: #000000;
    --ink-white: #ffffff;
    --caption-grey: #878383;
    --stripe-silver: #c9c9c9;
    --page: #ffffff;
  }
  html, body {
    margin: 0;
    width: 1200px;
    height: 759px;
    overflow: hidden;
    background: var(--page);
  }
  .banner-sheet { display: block; width: 1200px; height: 759px; }
  .fill-dark { fill: var(--panel-dark); }
  .fill-black { fill: var(--panel-black); }
  .fill-red { fill: var(--brand-red); }
  .frame-red { fill: none; stroke: var(--brand-red); stroke-width: 4; }
  .stripe { fill: var(--stripe-silver); }
  .wordmark { font-family: "Open Sans", sans-serif; font-weight: 400; fill: var(--ink-white); }
  .kpi { font-family: "PT Sans", sans-serif; font-weight: 700; fill: var(--ink-white); }
  .product-bold { font-family: "PT Sans", sans-serif; font-weight: 700; fill: var(--ink-white); }
  .product-light { font-family: "PT Sans Narrow", sans-serif; font-weight: 400; fill: #d8d8d8; }
  .product-narrow { font-family: "PT Sans Narrow", sans-serif; font-weight: 700; fill: var(--ink-white); }
  .cta { font-family: "PT Sans", sans-serif; font-weight: 700; fill: var(--ink-white); }
  .caption { font-family: "Open Sans", sans-serif; font-weight: 600; fill: var(--caption-grey); font-size: 44px; }
</style>
</head>
<body>
<svg class="banner-sheet" viewBox="0 0 1080 683" xmlns="http://www.w3.org/2000/svg">
  <defs>
    <clipPath id="leader-logo-clip"><rect x="35" y="37" width="727" height="88"/></clipPath>
    <clipPath id="rect-logo-clip"><rect x="67" y="248" width="298" height="248"/></clipPath>
    <clipPath id="tower-logo-clip"><rect x="771" y="35" width="119" height="599"/></clipPath>
  </defs>

  <!-- Leaderboard: logo -->
  <g class="leaderboard leaderboard--logo">
    <rect class="fill-dark" x="35" y="37" width="727" height="88"/>
    <circle class="fill-red" cx="140" cy="20" r="98" clip-path="url(#leader-logo-clip)"/>
    <text class="wordmark" x="710" y="104" font-size="54" text-anchor="end">brenwick</text>
  </g>

  <!-- Leaderboard: message -->
  <g class="leaderboard leaderboard--offer">
    <rect class="fill-dark" x="35" y="137" width="727" height="88"/>
    <polygon class="fill-red" points="35,137 70,137 35,225"/>
    <polygon class="fill-red" points="646,137 762,137 762,225 590,225"/>
    <polygon class="stripe" points="640,137 648,137 592,225 584,225"/>
    <text class="kpi" x="88" y="213" font-size="82">KPI</text>
    <text class="product-bold" x="255" y="177" font-size="37">Management</text>
    <text class="product-bold" x="255" y="215" font-size="37">Software</text>
    <text class="cta" x="750" y="177" font-size="38" text-anchor="end">FREE</text>
    <text class="cta" x="750" y="212" font-size="38" text-anchor="end">TRIAL</text>
  </g>

  <!-- Rectangle: logo -->
  <g class="rectangle rectangle--logo">
    <rect class="fill-black" x="67" y="248" width="298" height="248"/>
    <circle class="fill-red" cx="140" cy="250" r="76" clip-path="url(#rect-logo-clip)"/>
    <rect class="frame-red" x="69" y="250" width="294" height="244"/>
    <text class="wordmark" x="91" y="458" font-size="50">brenwick</text>
  </g>

  <!-- Rectangle: message -->
  <g class="rectangle rectangle--offer">
    <rect class="fill-black" x="369" y="248" width="298" height="248"/>
    <polygon class="fill-red" points="548,405 667,405 667,496 460,496"/>
    <polygon class="stripe" points="541,405 549,405 462,494 454,494"/>
    <rect class="frame-red" x="371" y="250" width="294" height="244"/>
    <text class="kpi" x="384" y="337" font-size="84">KPI</text>
    <text class="product-light" x="384" y="375" font-size="38">Management</text>
    <text class="product-light" x="384" y="414" font-size="38">Software</text>
    <text class="cta" x="645" y="446" font-size="36" text-anchor="end">FREE</text>
    <text class="cta" x="645" y="480" font-size="36" text-anchor="end">TRIAL</text>
  </g>

  <!-- Tower: logo -->
  <g class="tower tower--logo">
    <rect class="fill-dark" x="771" y="35" width="119" height="599"/>
    <circle class="fill-red" cx="862" cy="68" r="88" clip-path="url(#tower-logo-clip)"/>
    <text class="wordmark" x="786" y="444" font-size="40">bren</text>
    <text class="wordmark" x="786" y="487" font-size="40">wick</text>
  </g>

  <!-- Tower: message -->
  <g class="tower tower--offer">
    <rect class="fill-dark" x="900" y="35" width="120" height="599"/>
    <polygon class="fill-red" points="900,35 1020,35 900,145"/>
    <polygon class="fill-red" points="942,573 1020,573 1020,634 900,634 900,613"/>
    <polygon class="stripe" points="936,573 944,573 904,611 900,611 900,607"/>
    <text class="kpi" x="911" y="345" font-size="60">KPI</text>
    <text class="product-narrow" x="913" y="377" font-size="22">Management</text>
    <text class="product-narrow" x="913" y="404" font-size="24">Software</text>
    <text class="cta" x="1008" y="600" font-size="25" text-anchor="end">FREE</text>
    <text class="cta" x="1008" y="625" font-size="25" text-anchor="end">TRIAL</text>
  </g>

  <!-- Sheet caption -->
  <text class="caption" x="55" y="570">KPI Management Software -</text>
  <text class="caption" x="55" y="625">Ad Banner Samples</text>
</svg>
</body>
</html>
```